Scientific business journal infographics

We are writing a scientific article for an Academic Journal (such as the Ostrander Commerce Digest, a Business Book or the Wexley Trade Gazette). This article contains 9 infographics. We have created the graphics, and they convey the correct information and have the correct text, but they are lacking in an over-arching design and style that is clear, clean and business-like. The graphics we have created were made using a combination of Powerpoint objects and organic shapes using an AI engine. The organic shapes were deliberately made to depict the part of the process that is organic, flowing and has a level of unpredictability. As opposed to the much more rigid and linear part of the processes depicted using the Powerpoint objects.

We would like to see designs that preserve this combination of rigid process and organic process, that are clear, clean, and look well-designed and professional. These will be used in scientific business journals, and need to look like they belong there.

The designs need to have editable text, and could ideally be delivered back using a combination of images put into Powerpoint slides. We will also consider other formats, as long as we can edit them using readily available software (google cloud, MSFT 365, etc)

Font styles to use
Sans Serif

Colors

Requirements
Must have
• The sample graphics have very deliberate shapes and layouts that convey the scientific intent. Try to preserve the intent and do not reimagine the graphics or stray too far from the structure provided.

```html
<!DOCTYPE html>
<html lang="en">
<head>
<meta charset="utf-8">
<title>Ecostructure of Strategy – Infographic Set</title>
<link href="https://fonts.googleapis.com/css2?family=Montserrat:wght@700;800;900&family=Open+Sans:ital,wght@0,400;0,600;0,700;1,600;1,700&display=swap" rel="stylesheet">
<style>
  :root{
    --board:#474747;
    --paper:#ffffff;
    --navy:#155a7c;
    --navy-deep:#0f2a40;
    --steel:#6f8fa8;
    --grey:#9aa1ab;
    --grey-light:#b9bec6;
    --ink:#2b2b2b;
    --ink-soft:#555b63;
    --blue:#3a8fd6;
    --blue-fill:#4d95da;
    --orange:#e8742c;
    --teal:#2aa6c6;
    --green:#2e8b3e;
    --red:#e02020;
    --purple:#9a6ee8;
    --gold:#d9a520;
    --indigo:#5569e0;
    --tag:#f5c400;
    --ribbon-blue:#1f56a8;
  }
  *{box-sizing:border-box;margin:0;padding:0}
  html,body{width:1200px;height:738px;overflow:hidden}
  body{background:var(--board);position:relative;font-family:"Open Sans",Arial,sans-serif}
  .slide{position:absolute;width:352px;height:198px;background:var(--paper);overflow:hidden}
  .slide svg{display:block;width:352px;height:198px}
  .col-1{left:49px}.col-2{left:424px}.col-3{left:800px}
  .row-1{top:48px}.row-2{top:270px}.row-3{top:492px}
  .defs{position:absolute;width:0;height:0}
  svg text{font-family:"Open Sans",Arial,sans-serif}
  .head{font-family:"Montserrat",Arial,sans-serif;font-weight:800}
  .title{font-family:"Montserrat",Arial,sans-serif;font-weight:900;font-size:27px;fill:#111}
  .label-lg{font-weight:800;font-size:19px}
  .body{font-size:10.5px;fill:var(--ink)}
  .stage{font-family:"Montserrat",Arial,sans-serif;font-weight:700;font-size:11px}
  .iter{font-family:"Montserrat",Arial,sans-serif;font-weight:700;font-size:10px}
  .node{font-weight:600;font-size:20px;fill:#fff}
  .mini{font-style:italic;font-weight:600;font-size:8.5px;fill:#fff}
  .micro{font-size:7.5px;fill:#1d2b36}
  .tag-text{font-weight:600;font-size:10.5px;fill:#111}
  .trait{font-weight:700;font-size:10.5px;fill:#fff}
  .ribbon-label{font-size:10px;font-weight:600;fill:#fff}
</style>
</head>
<body>

<svg class="defs" aria-hidden="true">
  <defs>
    <marker id="arrow-purple" viewBox="0 0 10 10" refX="9" refY="5" markerWidth="5" markerHeight="5" orient="auto"><path d="M0,0 L10,5 L0,10z" fill="#9a6ee8"/></marker>
    <marker id="arrow-gold" viewBox="0 0 10 10" refX="9" refY="5" markerWidth="5" markerHeight="5" orient="auto"><path d="M0,0 L10,5 L0,10z" fill="#d9a520"/></marker>
    <marker id="arrow-indigo" viewBox="0 0 10 10" refX="9" refY="5" markerWidth="5" markerHeight="5" orient="auto"><path d="M0,0 L10,5 L0,10z" fill="#5569e0"/></marker>
    <marker id="arrow-navy" viewBox="0 0 10 10" refX="9" refY="5" markerWidth="5" markerHeight="5" orient="auto"><path d="M0,0 L10,5 L0,10z" fill="#155a7c"/></marker>
    <marker id="arrow-teal" viewBox="0 0 10 10" refX="9" refY="5" markerWidth="5" markerHeight="5" orient="auto"><path d="M0,0 L10,5 L0,10z" fill="#2aa6c6"/></marker>
    <marker id="arrow-green" viewBox="0 0 10 10" refX="9" refY="5" markerWidth="5" markerHeight="5" orient="auto"><path d="M0,0 L10,5 L0,10z" fill="#2e8b3e"/></marker>
    <marker id="arrow-red" viewBox="0 0 10 10" refX="9" refY="5" markerWidth="5" markerHeight="5" orient="auto"><path d="M0,0 L10,5 L0,10z" fill="#e02020"/></marker>
    <marker id="arrow-white" viewBox="0 0 10 10" refX="9" refY="5" markerWidth="4" markerHeight="4" orient="auto-start-reverse"><path d="M0,0 L10,5 L0,10z" fill="#fff"/></marker>
    <marker id="arrow-black" viewBox="0 0 10 10" refX="9" refY="5" markerWidth="5" markerHeight="5" orient="auto"><path d="M0,0 L10,5 L0,10z" fill="#111"/></marker>

    <radialGradient id="vortex" cx="50%" cy="50%" r="50%">
      <stop offset="0" stop-color="#cfe3f2"/>
      <stop offset="0.35" stop-color="#5d8fb6"/>
      <stop offset="0.75" stop-color="#1d3d5c"/>
      <stop offset="1" stop-color="#0d1c2d"/>
    </radialGradient>
    <linearGradient id="water" x1="0" y1="0" x2="1" y2="1">
      <stop offset="0" stop-color="#e3eff7"/>
      <stop offset="0.5" stop-color="#86b5d6"/>
      <stop offset="1" stop-color="#3e7ca8"/>
    </linearGradient>
    <linearGradient id="ribbon" x1="0" y1="1" x2="1" y2="0">
      <stop offset="0" stop-color="#1a4fa0"/>
      <stop offset="1" stop-color="#6aa2d8"/>
    </linearGradient>

    <symbol id="strategy-wheel" viewBox="-150 -150 300 300">
      <g fill="none">
        <circle r="110" stroke="#155a7c" stroke-width="72" pathLength="360" stroke-dasharray="57 303" stroke-dashoffset="88.5"/>
        <circle r="110" stroke="#9aa1ab" stroke-width="72" pathLength="360" stroke-dasharray="57 303" stroke-dashoffset="28.5"/>
        <circle r="110" stroke="#155a7c" stroke-width="72" pathLength="360" stroke-dasharray="57 303" stroke-dashoffset="-31.5"/>
        <circle r="110" stroke="#9aa1ab" stroke-width="72" pathLength="360" stroke-dasharray="57 303" stroke-dashoffset="-91.5"/>
        <circle r="110" stroke="#155a7c" stroke-width="72" pathLength="360" stroke-dasharray="57 303" stroke-dashoffset="-151.5"/>
        <circle r="110" stroke="#9aa1ab" stroke-width="72" pathLength="360" stroke-dasharray="57 303" stroke-dashoffset="-211.5"/>
        <circle r="55" stroke="#155a7c" stroke-width="20" pathLength="360" stroke-dasharray="57 303" stroke-dashoffset="88.5"/>
        <circle r="55" stroke="#9aa1ab" stroke-width="20" pathLength="360" stroke-dasharray="57 303" stroke-dashoffset="28.5"/>
        <circle r="55" stroke="#155a7c" stroke-width="20" pathLength="360" stroke-dasharray="57 303" stroke-dashoffset="-31.5"/>
        <circle r="55" stroke="#9aa1ab" stroke-width="20" pathLength="360" stroke-dasharray="57 303" stroke-dashoffset="-91.5"/>
        <circle r="55" stroke="#155a7c" stroke-width="20" pathLength="360" stroke-dasharray="57 303" stroke-dashoffset="-151.5"/>
        <circle r="55" stroke="#9aa1ab" stroke-width="20" pathLength="360" stroke-dasharray="57 303" stroke-dashoffset="-211.5"/>
      </g>
      <circle r="38" fill="#fff"/>
      <g fill="none" stroke="#fff" stroke-width="3" stroke-linecap="round">
        <g transform="translate(55,-95)"><circle r="13"/><circle r="6"/><path d="M0,-19v-4M19,0h4M-19,0h-4M13,-13l3,-3M-13,-13l-3,-3"/></g>
        <g transform="translate(110,0)"><rect x="-14" y="-10" width="28" height="18" rx="2"/><path d="M-6,14h12M0,8v6"/><circle cx="0" cy="-1" r="4"/></g>
        <g transform="translate(55,95)"><path d="M0,-14a9,9 0 0 1 9,9c0,7 -9,17 -9,17s-9,-10 -9,-17a9,9 0 0 1 9,-9z"/><circle cy="-5" r="3"/><path d="M-15,14h30"/></g>
        <g transform="translate(-55,95)"><rect x="-10" y="-14" width="20" height="26" rx="2"/><rect x="-15" y="-9" width="20" height="26" rx="2"/><path d="M-10,2h10M-10,8h10"/></g>
        <g transform="translate(-110,0)"><path d="M0,16v-14M0,2l-10,-10M0,2l10,-10M-14,-8h5v5M14,-8h-5v5"/></g>
        <g transform="translate(-55,-95)"><circle cy="-2" r="5"/><path d="M-10,12c0,-7 20,-7 20,0"/><path d="M-18,-14l3,3l5,-6M12,-17l6,6M18,-17l-6,6"/></g>
      </g>
    </symbol>

    <symbol id="iteration-left" viewBox="0 0 10 110">
      <text class="iter" text-anchor="middle" x="5" y="9">I<tspan x="5" dy="12">T</tspan><tspan x="5" dy="12">E</tspan><tspan x="5" dy="12">R</tspan><tspan x="5" dy="12">A</tspan><tspan x="5" dy="12">T</tspan><tspan x="5" dy="12">I</tspan><tspan x="5" dy="12">O</tspan><tspan x="5" dy="12">N</tspan></text>
    </symbol>
  </defs>
</svg>

<!-- Six levers of strategy -->
<section class="slide col-1 row-1" aria-label="Six levers of strategy">
  <svg viewBox="0 0 720 405">
    <use href="#strategy-wheel" x="182" y="53" width="300" height="300"/>
    <text class="head label-lg" x="200" y="45" text-anchor="end" fill="var(--grey)">DECISIONS</text>
    <text class="body" text-anchor="end"><tspan x="200" y="67">Execution of critical</tspan><tspan x="200" y="80">decision-making</tspan><tspan x="200" y="93">processes.</tspan></text>
    <text class="head label-lg" x="461" y="45" fill="var(--navy)">IDEAS</text>
    <text class="body"><tspan x="461" y="67">Conceptualization of</tspan><tspan x="461" y="80">individual ideas and</tspan><tspan x="461" y="93">micro strategies.</tspan></text>
    <text class="head label-lg" x="155" y="184" text-anchor="end" fill="var(--navy)">DIRECTION</text>
    <text class="body" text-anchor="end"><tspan x="155" y="201">Provision of</tspan><tspan x="155" y="214">guidance and</tspan><tspan x="155" y="227">directives.</tspan></text>
    <text class="head label-lg" x="504" y="172" fill="var(--grey)">MEMES</text>
    <text class="body"><tspan x="504" y="190">Integration into organizational</tspan><tspan x="504" y="203">lexicon and behavioural</tspan><tspan x="504" y="216">patterns, incl. social cues</tspan><tspan x="504" y="229">signalling the do's and don'ts</tspan><tspan x="504" y="242">of what is deemed as "acceptable"</tspan><tspan x="504" y="255">or "normal" behaviour</tspan></text>
    <text class="head label-lg" x="200" y="329" text-anchor="end" fill="var(--grey)">STORIES</text>
    <text class="body" text-anchor="end"><tspan x="200" y="347">Creation of coherent</tspan><tspan x="200" y="360">and adaptable</tspan><tspan x="200" y="373">narratives.</tspan></text>
    <text class="head label-lg" x="463" y="329" fill="var(--navy)">MAPS</text>
    <text class="body"><tspan x="463" y="347">Development of</tspan><tspan x="463" y="360">future state</tspan><tspan x="463" y="373">roadmaps.</tspan></text>
  </svg>
</section>

<!-- Ecostructure of strategy -->
<section class="slide col-2 row-1" aria-label="The ecostructure of strategy">
  <svg viewBox="0 0 720 405">
    <text class="title" x="366" y="48" text-anchor="middle">THE ECOSTRUCTURE OF STRATEGY</text>
    <g stroke="#1f4e6e" stroke-width="1.5" stroke-dasharray="5 4">
      <ellipse cx="125" cy="212" rx="140" ry="148" fill="#efefef"/>
      <ellipse cx="401" cy="200" rx="138" ry="114" fill="#d9d9d9" fill-opacity="0.9"/>
      <ellipse cx="640" cy="210" rx="130" ry="104" fill="var(--blue-fill)"/>
    </g>
    <g stroke="#444" stroke-width="1" stroke-dasharray="3 3">
      <line x1="263" y1="62" x2="263" y2="405"/>
      <line x1="507" y1="62" x2="507" y2="405"/>
    </g>
    <g stroke="#fff" stroke-width="2">
      <circle cx="133" cy="207" r="22" fill="var(--navy)"/>
      <circle cx="227" cy="207" r="22" fill="var(--grey)"/>
      <circle cx="309" cy="207" r="22" fill="var(--navy)"/>
      <circle cx="462" cy="207" r="22" fill="var(--grey)"/>
      <circle cx="562" cy="207" r="22" fill="var(--navy)"/>
      <circle cx="666" cy="207" r="22" fill="var(--grey)"/>
    </g>
    <g fill="none" stroke="#fff" stroke-width="2" stroke-linecap="round">
      <g transform="translate(133,207)"><circle r="7"/><path d="M0,-11v-3M11,0h3M-11,0h-3"/></g>
      <g transform="translate(227,207)"><rect x="-9" y="-7" width="18" height="12" rx="1"/><path d="M-4,9h8"/></g>
      <g transform="translate(309,207)"><path d="M0,-10a6,6 0 0 1 6,6c0,5 -6,12 -6,12s-6,-7 -6,-12a6,6 0 0 1 6,-6z"/></g>
      <g transform="translate(462,207)"><rect x="-7" y="-10" width="14" height="18" rx="1"/><path d="M-4,-2h8M-4,3h8"/></g>
      <g transform="translate(562,207)"><path d="M0,11v-9M0,2l-7,-7M0,2l7,-7"/></g>
      <g transform="translate(666,207)"><circle cy="-2" r="4"/><path d="M-7,9c0,-5 14,-5 14,0"/></g>
    </g>
    <g font-size="16">
      <text x="133" y="248" text-anchor="middle" fill="#1e5f86">IDEAS</text>
      <text x="227" y="248" text-anchor="middle" fill="#7a818a">MEME</text>
      <text x="309" y="248" text-anchor="middle" fill="#1e5f86">MAPS</text>
      <text x="462" y="248" text-anchor="middle" fill="#7a818a">STORIE</text>
      <text x="562" y="248" text-anchor="middle" fill="#1e5f86">DIRECTIONS</text>
      <text x="666" y="248" text-anchor="middle" fill="#7a818a">DECISIONS</text>
    </g>
    <g class="stage" text-anchor="middle">
      <text x="133" y="373" fill="#111">ECOSYSTEM OF</text>
      <text x="133" y="388" fill="var(--blue)">EMERGENCE</text>
      <text x="389" y="373" fill="#111">ECOSYSTEM OF</text>
      <text x="389" y="388" fill="var(--orange)">(RE-/DE-) STRUCTURING</text>
      <text x="616" y="373" fill="#111">ECOSYSTEM OF</text>
      <text x="616" y="388" fill="var(--blue)">REIFICATION</text>
    </g>
  </svg>
</section>

<!-- Actors, actions, artifacts -->
<section class="slide col-3 row-1" aria-label="Actors, actions and artifacts cycle">
  <svg viewBox="0 0 720 405">
    <circle cx="358" cy="201" r="180" fill="url(#vortex)" role="img" aria-label="Swirling water vortex around the strategy wheel"/>
    <g fill="none" stroke="#fff" stroke-width="2" marker-end="url(#arrow-white)" marker-start="url(#arrow-white)">
      <path d="M285,80 A150,150 0 0 0 197,228"/>
      <path d="M428,78 A150,150 0 0 1 507,228"/>
      <path d="M278,338 A150,150 0 0 0 440,340"/>
      <path d="M358,112 V140"/>
    </g>
    <use href="#strategy-wheel" x="290" y="133" width="136" height="136"/>
    <g class="mini" text-anchor="middle">
      <text x="333" y="150">Decision</text><text x="381" y="150">Ideas</text>
      <text x="300" y="191">Direction</text><text x="420" y="192">Memes</text>
      <text x="336" y="265">Stories</text><text x="382" y="265">Maps</text>
    </g>
    <g fill="var(--navy)" stroke="#0b2233" stroke-width="2">
      <circle cx="360" cy="62" r="47"/><circle cx="221" cy="292" r="47"/><circle cx="495" cy="290" r="47"/>
    </g>
    <g class="node" text-anchor="middle">
      <text x="360" y="69">Actors</text><text x="221" y="299">Actions</text><text x="495" y="297">Artifacts</text>
    </g>
  </svg>
</section>

<!-- Catalyzers -->
<section class="slide col-1 row-2" aria-label="Catalyzers within the actors, actions and artifacts cycle">
  <svg viewBox="0 0 720 405">
    <circle cx="360" cy="207" r="180" fill="url(#vortex)" role="img" aria-label="Swirling water vortex around the strategy wheel"/>
    <g fill="none" stroke="#fff" stroke-width="2" marker-end="url(#arrow-white)" marker-start="url(#arrow-white)">
      <path d="M285,85 A150,150 0 0 0 197,232"/>
      <path d="M430,84 A150,150 0 0 1 512,232"/>
      <path d="M280,345 A150,150 0 0 0 442,346"/>
      <path d="M360,114 V140"/>
    </g>
    <use href="#strategy-wheel" x="292" y="139" width="136" height="136"/>
    <g class="mini" text-anchor="middle">
      <text x="333" y="152">Decision</text><text x="382" y="152">Ideas</text>
      <text x="300" y="193">Direction</text><text x="420" y="193">Memes</text>
      <text x="336" y="265">Stories</text><text x="382" y="265">Maps</text>
    </g>
    <text x="446" y="153" font-style="italic" font-weight="700" font-size="14" fill="#fff" text-anchor="middle">Catalyzers</text>
    <g fill="var(--navy)" stroke="#0b2233" stroke-width="2">
      <circle cx="360" cy="62" r="47"/><circle cx="221" cy="293" r="47"/><circle cx="495" cy="290" r="47"/>
    </g>
    <g class="node" text-anchor="middle">
      <text x="360" y="69">Actors</text><text x="221" y="300">Actions</text><text x="495" y="297">Artifacts</text>
    </g>
  </svg>
</section>

<!-- Strategy stages with imagery -->
<section class="slide col-2 row-2" aria-label="Iterative strategy stages">
  <svg viewBox="0 0 720 405">
    <g class="stage" text-anchor="middle">
      <text x="158" y="72" fill="var(--teal)">NURTURING</text><text x="158" y="85" fill="var(--teal)">STRATEGY</text>
      <text x="359" y="72" fill="var(--green)">(RE-)STRUCTURING</text><text x="359" y="85" fill="var(--green)">STRATEGY</text>
      <text x="559" y="72" fill="var(--red)">DELIBERATE</text><text x="559" y="85" fill="var(--red)">STRATEGY</text>
      <text x="158" y="326" fill="#1e5f86">EMERGENT</text><text x="158" y="339" fill="#1e5f86">STRATEGY</text>
      <text x="359" y="326" fill="#1e5f86">(DE-)STRUCTURING</text><text x="359" y="339" fill="#1e5f86">STRATEGY</text>
      <text x="552" y="326" fill="#1e5f86">OPENING</text><text x="552" y="339" fill="#1e5f86">STRATEGY</text>
    </g>
    <g fill="none" stroke-width="1.6">
      <path d="M32,150 V82 H97" stroke="var(--teal)" marker-end="url(#arrow-teal)"/>
      <path d="M215,82 H295" stroke="var(--green)" marker-end="url(#arrow-green)"/>
      <path d="M415,82 H495" stroke="var(--red)" marker-end="url(#arrow-red)"/>
      <path d="M686,272 V334 H622" stroke="#1e5f86" marker-end="url(#arrow-navy)"/>
      <path d="M503,334 H425" stroke="#1e5f86" marker-end="url(#arrow-navy)"/>
      <path d="M292,334 H215" stroke="#1e5f86" marker-end="url(#arrow-navy)"/>
    </g>
    <use href="#iteration-left" x="26" y="157" width="12" height="110" fill="var(--teal)"/>
    <use href="#iteration-left" x="680" y="142" width="12" height="110" fill="var(--teal)"/>
    <rect x="62" y="107" width="192" height="190" rx="8" fill="#d8e6ef" stroke="#7ba9c9" stroke-width="2" role="img" aria-label="Target with arrow on a digital blueprint background"/>
    <rect x="263" y="107" width="191" height="190" rx="8" fill="#ece8f2" stroke="#3c8a4a" stroke-width="2" role="img" aria-label="Clock face with a chess king at its centre"/>
    <rect x="464" y="107" width="191" height="190" rx="8" fill="#2c2c2c" stroke="var(--red)" stroke-width="2" role="img" aria-label="Chalk tic-tac-toe grid with a red heart"/>
  </svg>
</section>

<!-- Infinity loop of strategy -->
<section class="slide col-3 row-2" aria-label="Infinity loop of strategy stages">
  <svg viewBox="0 0 720 405">
    <g stroke="#444" stroke-width="1" stroke-dasharray="3 3">
      <line x1="240" y1="0" x2="240" y2="405"/><line x1="480" y1="0" x2="480" y2="405"/>
    </g>
    <path d="M360,200 C420,100 610,80 610,200 C610,320 420,300 360,200 C300,100 110,80 110,200 C110,320 300,300 360,200Z" fill="none" stroke="url(#water)" stroke-width="40" role="img" aria-label="Flowing water infinity loop with an upward arrow"/>
    <g class="stage" text-anchor="middle">
      <text x="162" y="33" fill="var(--purple)">NURTURING</text><text x="162" y="45" fill="var(--purple)">STRATEGY</text>
      <text x="363" y="33" fill="var(--gold)">(RE-)STRUCTURING</text><text x="363" y="45" fill="var(--gold)">STRATEGY</text>
      <text x="563" y="33" fill="var(--indigo)">DELIBERATE</text><text x="563" y="45" fill="var(--indigo)">STRATEGY</text>
      <text x="162" y="363" fill="#1e5f86">EMERGENT</text><text x="162" y="375" fill="#1e5f86">STRATEGY</text>
      <text x="363" y="363" fill="var(--gold)">(DE-)STRUCTURING</text><text x="363" y="375" fill="var(--gold)">STRATEGY</text>
      <text x="556" y="363" fill="var(--indigo)">OPENING</text><text x="556" y="375" fill="var(--indigo)">STRATEGY</text>
    </g>
    <g fill="none" stroke-width="1.6">
      <path d="M35,44 H110" stroke="var(--purple)" marker-end="url(#arrow-purple)"/>
      <path d="M220,44 H296" stroke="var(--gold)" marker-end="url(#arrow-gold)"/>
      <path d="M430,44 H507" stroke="var(--indigo)" marker-end="url(#arrow-indigo)"/>
      <path d="M110,372 H37" stroke="#1e5f86" marker-end="url(#arrow-navy)"/>
      <path d="M296,372 H220" stroke="var(--gold)" marker-end="url(#arrow-gold)"/>
      <path d="M506,372 H430" stroke="var(--indigo)" marker-end="url(#arrow-indigo)"/>
      <path d="M35,140 V62" stroke="#1e5f86" marker-end="url(#arrow-navy)"/>
      <path d="M684,288 V356" stroke="#1e5f86" marker-end="url(#arrow-navy)"/>
    </g>
    <use href="#iteration-left" x="29" y="150" width="12" height="110" fill="#1e5f86"/>
    <use href="#iteration-left" x="678" y="158" width="12" height="110" fill="#1e5f86"/>
  </svg>
</section>

<!-- Infinity loop with levers -->
<section class="slide col-1 row-3" aria-label="Infinity loop with strategy activities and levers">
  <svg viewBox="0 0 720 405">
    <g stroke="#444" stroke-width="1" stroke-dasharray="3 3">
      <line x1="240" y1="0" x2="240" y2="405"/><line x1="480" y1="0" x2="480" y2="405"/>
    </g>
    <path d="M360,200 C420,100 610,80 610,200 C610,320 420,300 360,200 C300,100 110,80 110,200 C110,320 300,300 360,200Z" fill="none" stroke="url(#water)" stroke-width="40" role="img" aria-label="Flowing water infinity loop with an upward arrow"/>
    <g class="stage" text-anchor="middle">
      <text x="162" y="35" fill="var(--purple)">NURTURING</text><text x="162" y="47" fill="var(--purple)">STRATEGY</text>
      <text x="363" y="35" fill="var(--gold)">(RE-)STRUCTURING</text><text x="363" y="47" fill="var(--gold)">STRATEGY</text>
      <text x="563" y="35" fill="var(--indigo)">DELIBERATE</text><text x="563" y="47" fill="var(--indigo)">STRATEGY</text>
      <text x="162" y="364" fill="#1e5f86">EMERGENT</text><text x="162" y="376" fill="#1e5f86">STRATEGY</text>
      <text x="363" y="364" fill="var(--gold)">(DE-)STRUCTURING</text><text x="363" y="376" fill="var(--gold)">STRATEGY</text>
      <text x="556" y="364" fill="var(--indigo)">OPENING</text><text x="556" y="376" fill="var(--indigo)">STRATEGY</text>
    </g>
    <g fill="none" stroke-width="1.6">
      <path d="M35,44 H110" stroke="var(--purple)" marker-end="url(#arrow-purple)"/>
      <path d="M220,44 H296" stroke="var(--gold)" marker-end="url(#arrow-gold)"/>
      <path d="M430,44 H507" stroke="var(--indigo)" marker-end="url(#arrow-indigo)"/>
      <path d="M110,373 H37" stroke="#1e5f86" marker-end="url(#arrow-navy)"/>
      <path d="M296,373 H220" stroke="var(--gold)" marker-end="url(#arrow-gold)"/>
      <path d="M506,373 H430" stroke="var(--indigo)" marker-end="url(#arrow-indigo)"/>
      <path d="M36,140 V62" stroke="#1e5f86" marker-end="url(#arrow-navy)"/>
      <path d="M684,290 V356" stroke="#1e5f86" marker-end="url(#arrow-navy)"/>
    </g>
    <use href="#iteration-left" x="30" y="150" width="12" height="110" fill="#1e5f86"/>
    <use href="#iteration-left" x="678" y="150" width="12" height="110" fill="#1e5f86"/>
    <g class="micro" text-anchor="middle">
      <text x="216" y="120">Activators</text><text x="174" y="134">Triggers</text><text x="150" y="153">Manifestors</text>
      <text x="307" y="146">Breakers</text><text x="406" y="154">Dampeners</text><text x="530" y="95">Confluencers</text>
      <text x="578" y="147">Channels</text><text x="386" y="183">Levers</text><text x="352" y="223">Architectures</text>
      <text x="135" y="224">Cognizers</text><text x="412" y="250">Cultivability</text><text x="566" y="261">Memories</text>
      <text x="144" y="267">Boosters</text><text x="450" y="290">Openness</text><text x="246" y="304">Anchors</text>
      <text x="206" y="312">Fortifier</text>
    </g>
    <g fill="var(--tag)">
      <rect x="245" y="104" width="68" height="16"/><rect x="402" y="114" width="70" height="16"/>
      <rect x="106" y="174" width="52" height="16"/><rect x="565" y="208" width="62" height="16"/>
      <rect x="298" y="241" width="60" height="16"/><rect x="108" y="281" width="64" height="16"/>
      <rect x="497" y="292" width="50" height="28"/>
    </g>
    <g class="tag-text" text-anchor="middle">
      <text x="279" y="116">Instigating</text><text x="437" y="126">Synergizing</text>
      <text x="132" y="186">Igniting</text><text x="596" y="220">Deploying</text>
      <text x="328" y="253">Adapting</text><text x="140" y="293">Nurturing</text>
      <text x="522" y="304">State</text><text x="522" y="316">sensing</text>
    </g>
  </svg>
</section>

<!-- Order and meaning progression -->
<section class="slide col-2 row-3" aria-label="Progression from old strategy to new strategy">
  <svg viewBox="0 0 720 405">
    <g fill="none" stroke="#111" stroke-width="1.8">
      <path d="M82,355 V58" marker-end="url(#arrow-black)"/>
      <path d="M82,355 H645" marker-end="url(#arrow-black)"/>
    </g>
    <text x="78" y="100" font-size="9.5" font-weight="600" fill="#111" transform="rotate(-90 78 100)">Order</text>
    <text x="606" y="367" font-size="9.5" font-weight="600" fill="#111">Meaning</text>
    <g role="img" aria-label="Blue ribbon rising from old strategy to new strategy">
      <path d="M100,352 C160,345 195,275 236,282 C268,288 262,318 300,318 C340,318 350,282 400,272 C450,262 480,200 505,140 C518,106 526,86 535,68" fill="none" stroke="url(#ribbon)" stroke-width="20" stroke-linecap="round"/>
      <ellipse cx="302" cy="322" rx="66" ry="22" fill="var(--ribbon-blue)"/>
      <rect x="348" y="262" width="104" height="20" rx="10" fill="var(--ribbon-blue)"/>
    </g>
    <g fill="url(#water)" opacity="0.85" role="img" aria-label="Small water infinity loops along the path">
      <ellipse cx="162" cy="282" rx="45" ry="15"/>
      <ellipse cx="268" cy="240" rx="52" ry="16"/>
      <ellipse cx="385" cy="190" rx="55" ry="17"/>
      <ellipse cx="480" cy="130" rx="58" ry="18"/>
    </g>
    <g fill="none" stroke="#111" stroke-width="1.5">
      <rect x="102" y="237" width="120" height="85" rx="8"/>
      <rect x="198" y="188" width="135" height="107" rx="8"/>
      <rect x="311" y="138" width="150" height="106" rx="8"/>
      <rect x="400" y="80" width="165" height="117" rx="8"/>
    </g>
    <g font-size="10.5" font-weight="600" fill="#111">
      <text x="115" y="229">Old Strategy</text>
      <text x="222" y="179">New Strategy</text>
    </g>
    <g class="ribbon-label" text-anchor="middle">
      <text x="400" y="276">Tipping Point</text>
      <text x="302" y="319">Letting go of Old</text>
      <text x="302" y="332">Emergence of New</text>
    </g>
  </svg>
</section>

<!-- Individual traits for systems thinking -->
<section class="slide col-3 row-3" aria-label="Individual traits that enable systems thinking">
  <svg viewBox="0 0 720 405">
    <g fill="none" transform="translate(360,202)">
      <circle r="129" stroke="var(--navy)" stroke-width="102" pathLength="360" stroke-dasharray="45 315" stroke-dashoffset="135"/>
      <circle r="126" stroke="var(--steel)" stroke-width="96" pathLength="360" stroke-dasharray="45 315" stroke-dashoffset="90"/>
      <circle r="132" stroke="var(--navy)" stroke-width="108" pathLength="360" stroke-dasharray="45 315" stroke-dashoffset="45"/>
      <circle r="115" stroke="#a9b0bb" stroke-width="74" pathLength="360" stroke-dasharray="45 315" stroke-dashoffset="0"/>
      <circle r="130" stroke="var(--navy)" stroke-width="104" pathLength="360" stroke-dasharray="45 315" stroke-dashoffset="-45"/>
      <circle r="121" stroke="var(--grey-light)" stroke-width="86" pathLength="360" stroke-dasharray="45 315" stroke-dashoffset="-90"/>
      <circle r="130" stroke="var(--navy)" stroke-width="104" pathLength="360" stroke-dasharray="45 315" stroke-dashoffset="-135"/>
      <circle r="119" stroke="#b5bac2" stroke-width="82" pathLength="360" stroke-dasharray="45 315" stroke-dashoffset="-180"/>
      <circle r="78" fill="#e3e6ea"/>
      <circle r="68" fill="#fff"/>
    </g>
    <g text-anchor="middle" font-weight="700" font-size="10.5" fill="#111">
      <text x="360" y="189">Individual Traits</text><text x="360" y="204">That Enable</text><text x="360" y="219">Systems Thinking</text>
    </g>
    <g class="trait" text-anchor="middle">
      <text x="319" y="72">Tolerance for</text><text x="319" y="87">Ambiguity</text>
      <text x="426" y="78">Curiosity</text>
      <text x="485" y="153">Openness</text>
      <text x="472" y="246">Strong</text><text x="472" y="261">Interpersonal</text><text x="472" y="276">Skills</text>
      <text x="398" y="310">Strong</text><text x="398" y="325">Communication</text><text x="398" y="340">Skills</text>
      <text x="296" y="307">Ask the Right</text><text x="296" y="322">Questions</text>
      <text x="233" y="220">Navigate</text><text x="233" y="235">Complexity</text>
      <text x="248" y="129">Analytical</text><text x="248" y="144">Ability</text>
    </g>
  </svg>
</section>

</body>
</html>
```